Holiday Card for Hydrographic Industry

Please design a holiday card that is not religious by nature. Incorporate our Seahorse if possible (business name is Thornbill Surveying). There are samples of last two years cards attached as well as our logo.

We are an international business with domestic and foreign clients so possibly something that relates internationally.

This card should be a 5x7 foldover card. Preferably a design on the front with a message of Happy Holidays or something to that nature, and writing on the inside, which I can provide. Most important is the outside design and something complimentary on the inside to accompany the writing.

Thanks!

Target Market(s)

Government, International Hydrographic Industry

Industry/Entity Type

Business

Font styles to use
Sans Serif

Requirements
Must have
• Whimsical holiday design on the front, logo inside with message
Nice to have
• May incorporate Seahorse into design on front
Should not have
• Religious tone

```html
<!DOCTYPE html>
<html lang="en">
<head>
<meta charset="utf-8">
<title>Thornbill Surveying – Holiday Card Front</title>
<link rel="stylesheet" href="https://fonts.googleapis.com/css2?family=Great+Vibes&family=Montserrat:wght@700&display=swap">
<style>
  :root {
    --navy-deep: #020c2e;
    --navy: #052a5e;
    --ocean: #0a5596;
    --ocean-bright: #1a86c4;
    --aqua: #4fc0ea;
    --sparkle: #e6f3fc;
    --white: #ffffff;
    --fold-mark: #e0358f;
  }
  * { box-sizing: border-box; margin: 0; padding: 0; }
  html, body {
    width: 1200px; height: 819px; overflow: hidden;
    background: #d9d9d9;
  }
  .card {
    position: relative;
    width: 1200px; height: 819px;
    overflow: hidden;
    background:
      radial-gradient(ellipse 38% 30% at 88% 52%, rgba(79,192,234,.75), transparent 75%),
      radial-gradient(ellipse 55% 22% at 30% 50%, rgba(26,134,196,.7), transparent 80%),
      linear-gradient(180deg, var(--navy) 0%, var(--ocean) 35%, var(--ocean-bright) 52%, var(--ocean) 66%, var(--navy) 82%, var(--navy-deep) 100%);
  }
  .bubble-field {
    position: absolute; left: 0; top: 0; width: 1200px; height: 420px;
    background:
      radial-gradient(ellipse 16% 26% at 6% 62%, rgba(230,243,252,.55), transparent 75%),
      radial-gradient(ellipse 20% 24% at 24% 58%, rgba(230,243,252,.7), transparent 75%),
      radial-gradient(ellipse 20% 22% at 42% 48%, rgba(230,243,252,.7), transparent 75%),
      radial-gradient(ellipse 18% 18% at 58% 36%, rgba(230,243,252,.65), transparent 75%),
      radial-gradient(ellipse 20% 20% at 74% 18%, rgba(230,243,252,.8), transparent 75%),
      radial-gradient(ellipse 18% 22% at 92% 20%, rgba(230,243,252,.75), transparent 75%),
      radial-gradient(ellipse 14% 16% at 84% 4%, rgba(255,255,255,.8), transparent 75%);
  }
  .fish-school {
    position: absolute; left: 0; top: 400px; width: 620px; height: 280px;
    background:
      radial-gradient(ellipse 45% 40% at 25% 45%, rgba(8,48,96,.6), transparent 75%),
      radial-gradient(ellipse 35% 30% at 55% 30%, rgba(8,48,96,.4), transparent 75%);
  }
  .scenery { position: absolute; left: 0; top: 0; }
  .seahorse {
    position: absolute;
    background:
      radial-gradient(ellipse 40% 30% at 50% 30%, rgba(255,255,255,.95), transparent 80%),
      linear-gradient(180deg, rgba(240,248,253,.85), rgba(200,230,248,.7));
    border-radius: 50% 50% 45% 45% / 28% 28% 40% 40%;
    box-shadow: 0 0 18px rgba(230,243,252,.5);
  }
  .seahorse--back { left: 262px; top: 420px; width: 84px; height: 272px; }
  .seahorse--front { left: 875px; top: 146px; width: 150px; height: 420px; }
  .company-name {
    position: absolute; left: 168px; top: 724px; width: 262px;
    font-family: "Montserrat", sans-serif; font-weight: 700;
    font-size: 21px; line-height: 23px; letter-spacing: 1.5px;
    color: var(--white); text-align: center; text-transform: uppercase;
  }
  .greeting {
    position: absolute; left: 0; top: 0; width: 1200px; height: 819px;
    font-family: "Great Vibes", cursive; font-weight: 400;
    color: var(--white);
  }
  .greeting span {
    position: absolute; font-size: 104px; line-height: 1; white-space: nowrap;
  }
  .greeting .greeting__first { left: 836px; top: 518px; }
  .greeting .greeting__second { left: 776px; top: 648px; }
</style>
</head>
<body>
  <main class="card">
    <div class="bubble-field" role="img" aria-label="Sparkling cloud of white air bubbles arching across the top of the card"></div>
    <div class="fish-school" role="img" aria-label="School of small fish swimming in the deep blue water"></div>

    <svg class="scenery" width="1200" height="819" viewBox="0 0 1200 819" aria-hidden="true">
      <path d="M0 690 C 140 640, 220 560, 330 560 S 600 520, 760 470 S 1080 410, 1200 400 L1200 819 L0 819 Z"
            fill="rgba(2,18,60,.5)"/>
      <path d="M0 640 C 130 560, 260 520, 420 545 S 700 470, 860 440 S 1100 410, 1200 400"
            fill="none" stroke="rgba(79,192,234,.8)" stroke-width="3"/>
      <path d="M150 650 C 260 560, 380 520, 520 540 S 740 500, 880 440"
            fill="none" stroke="rgba(255,255,255,.35)" stroke-width="1.5"/>
      <path d="M0 780 C 220 700, 460 680, 700 690 S 1040 660, 1200 580"
            fill="none" stroke="rgba(79,192,234,.35)" stroke-width="1.5"/>
      <g fill="rgba(255,255,255,.12)" stroke="rgba(255,255,255,.75)" stroke-width="1.5">
        <circle cx="1138" cy="340" r="24"/>
        <circle cx="1100" cy="392" r="11"/>
        <circle cx="1126" cy="412" r="6"/>
        <circle cx="1150" cy="452" r="16"/>
        <circle cx="1096" cy="470" r="8"/>
        <circle cx="1050" cy="500" r="22"/>
        <circle cx="1010" cy="560" r="9"/>
        <circle cx="988" cy="535" r="5"/>
        <circle cx="958" cy="565" r="6"/>
      </g>
      <line x1="599" y1="10" x2="599" y2="819" stroke="var(--fold-mark)" stroke-width="1.5" stroke-dasharray="10 8"/>
    </svg>

    <div class="seahorse seahorse--back" role="img" aria-label="White filigree seahorse illustration"></div>
    <p class="company-name">Thornbill Surveying</p>

    <div class="seahorse seahorse--front" role="img" aria-label="Large white filigree seahorse illustration among bubbles"></div>
    <h1 class="greeting"><span class="greeting__first">Happy</span><span class="greeting__second">Holidays!</span></h1>
  </main>
</body>
</html>
```